Rolo Fenu bar restaurant japanese street food

Hello dear friends!

We are a Gyoza Bar, specializing in square sandwiches (made with Hokkaido bread) and gyoza dumplings.

Our interior is designed to look like a Japanese street, with many signboards, street signs, and urban elements. We will attach photos so you can capture the overall vibe and atmosphere.

Our kitchen concept is street food.

Today we have a task to develop a takeaway / delivery box for our food.

We truly love our product and want to give it a professional and distinctive presentation.

Custom packaging is an important part of our brand style.

We appreciate non-standard solutions, shapes, and sizes.

About our product
We are a Gyoza Bar, and we have several types of gyoza:

Beef

Pork

Chicken

Vegetable

Salmon & Shrimp

What we need
We need one universal box for all flavors, with flavor indicators that we can mark when assembling an order.

A standard portion contains 6 dumplings.

Size of one dumpling:

Length: 7.5 cm

Height: 3.5 cm

Inside the box
The box must include:

An integrated sauce container

Diameter: 6 cm

Height: 3 cm

Shape: wider toward the top than the bottom

Chopsticks placed inside the box

Dividers between dumplings so they do not stick together

We imagine the box as a long rectangular shape.

Multiple portions
If an order includes several portions, the boxes should be able to connect or stack together.

For example:

stacking one box on top of another

small locking tabs or “ears” that allow the boxes to be connected together

You will see reference examples in the attachments.

Design
The design direction is up to you, as we like both:

minimalist concepts

more detailed / graphic designs

The most important thing is:
please do not make the logo too small, because it needs to remain clearly readable.

Final deliverable
The final result should be a packaging dieline (flat layout) that we can send directly to production without additional questions.

Thank you all for your attention and good luck!
If you have any questions, we will be happy to answer them.

P.S.

We also need a second box for other dishes with the following dimensions:

12.5 cm × 12.5 cm
Height: 7 cm

Target Market(s)

Please note that we are a high-quality street food brand. Packaging is part of our identity. We communicate through packaging

Requirements
Must have
• Chopsticks and a sauce container must be integrated into the packaging.

```html
<!DOCTYPE html>
<html lang="en">
<head>
<meta charset="utf-8">
<title>Rolo Fenu – Gyoza Box</title>
<link rel="stylesheet" href="https://fonts.googleapis.com/css2?family=Montserrat:wght@600;700;800;900&family=Noto+Sans+JP:wght@500&display=swap">
<style>
  :root {
    --ink: #0d0d0d;
    --charcoal: #2e2927;
    --cream: #fdf5ee;
    --paper: #efe7df;
    --red: #e2352c;
    --deep-red: #be1f1b;
    --tab: #4a4542;
    --strip: #2a2828;
  }
  * { margin: 0; padding: 0; box-sizing: border-box; }
  html, body { width: 1200px; height: 1000px; overflow: hidden; background: #000; }
  body { position: relative; font-family: "Montserrat", sans-serif; }

  .lid-edge { position: absolute; left: 78px; top: 0; width: 1068px; height: 45px; background: var(--strip); }

  .lid-top { position: absolute; left: 78px; top: 45px; width: 1045px; height: 422px; background: var(--cream); }

  .sauce-slot { position: absolute; left: 25px; top: 24px; width: 271px; height: 251px; background: var(--red); }
  .sauce-slot__well {
    position: absolute; left: 21px; top: 10px; width: 230px; height: 230px; border-radius: 50%;
    background: var(--charcoal); color: var(--cream);
    display: flex; align-items: center; justify-content: center; text-align: center;
    font-weight: 700; font-size: 21px; line-height: 24px; letter-spacing: 0.5px;
  }

  .flavours { position: absolute; left: 37px; top: 292px; width: 280px; height: 110px; }
  .flavour { position: absolute; display: flex; align-items: flex-start; font-weight: 700; font-size: 17px; line-height: 19px; color: var(--ink); letter-spacing: 0.4px; }
  .flavour__box { width: 18px; height: 18px; border: 1.5px solid var(--ink); margin-right: 9px; flex: none; }
  .flavour--beef { left: 0; top: 0; }
  .flavour--pork { left: 0; top: 38px; }
  .flavour--chicken { left: 0; top: 76px; }
  .flavour--veg { left: 134px; top: 0; }
  .flavour--seafood { left: 134px; top: 38px; }

  .brand-mark { position: absolute; left: 337px; top: 20px; width: 310px; height: 352px; display: flex; flex-direction: column; align-items: center; justify-content: center; }
  .brand-mark__square { width: 70px; height: 70px; background: var(--red); margin-bottom: 26px; }
  .brand-mark__name { font-weight: 900; font-size: 74px; line-height: 78px; color: var(--ink); text-align: center; letter-spacing: 1px; }

  .street-scene {
    position: absolute; left: 662px; top: 30px; width: 350px; height: 375px;
    background: linear-gradient(160deg, #efe5dc 0%, #d9cfc6 45%, #c94a3f 80%, #2a2626 100%);
  }

  .box-side { position: absolute; left: 78px; top: 516px; width: 1040px; height: 151px; }
  .box-side__rim { position: absolute; left: 0; top: 0; width: 100%; height: 24px; background: var(--paper); }
  .box-side__lip { position: absolute; left: 0; top: 24px; width: 100%; height: 25px; background: #f7f0e8; }
  .box-side__panel { position: absolute; left: 0; top: 49px; width: 100%; height: 102px; background: var(--deep-red); }
  .box-side__tab { position: absolute; top: 2px; width: 84px; height: 20px; border: 2px solid var(--tab); border-bottom: none; }
  .box-side__tab--left { left: 170px; }
  .box-side__tab--right { left: 794px; }
  .box-side__latch { position: absolute; left: 442px; top: 49px; width: 122px; height: 70px; background: #d12a24; border: 1px solid #9d1814; }
  .box-side__latch-top { position: absolute; left: 444px; top: 49px; width: 44px; height: 12px; background: #1b1b1b; }

  .box-side__name { position: absolute; left: 92px; top: 62px; font-weight: 900; font-size: 38px; line-height: 38px; color: var(--cream); letter-spacing: 1px; }
  .box-side__jp { position: absolute; left: 590px; top: 70px; width: 440px; font-family: "Noto Sans JP", sans-serif; font-weight: 500; font-size: 29px; line-height: 36px; color: var(--cream); text-align: center; letter-spacing: 1px; }
  .box-side__tagline { position: absolute; left: 590px; top: 109px; width: 440px; font-weight: 800; font-size: 15px; line-height: 18px; color: var(--cream); text-align: center; letter-spacing: 0.6px; }
</style>
</head>
<body>
  <div class="lid-edge"></div>

  <section class="lid-top">
    <div class="sauce-slot">
      <div class="sauce-slot__well">SAUCE<br>CONTAINER<br>HERE</div>
    </div>

    <div class="flavours">
      <div class="flavour flavour--beef"><span class="flavour__box"></span>Beef</div>
      <div class="flavour flavour--pork"><span class="flavour__box"></span>Pork</div>
      <div class="flavour flavour--chicken"><span class="flavour__box"></span>Chicken</div>
      <div class="flavour flavour--veg"><span class="flavour__box"></span>Vegetable</div>
      <div class="flavour flavour--seafood"><span class="flavour__box"></span>Salmon &amp;<br>Shrimp</div>
    </div>

    <div class="brand-mark">
      <div class="brand-mark__square"></div>
      <div class="brand-mark__name">ROLO<br>FENU</div>
    </div>

    <div class="street-scene" role="img" aria-label="Illustration of a busy Japanese street with signboards and a young man eating gyoza, in red, black and cream"></div>
  </section>

  <section class="box-side">
    <div class="box-side__rim"></div>
    <div class="box-side__tab box-side__tab--left"></div>
    <div class="box-side__tab box-side__tab--right"></div>
    <div class="box-side__lip"></div>
    <div class="box-side__panel"></div>
    <div class="box-side__latch"></div>
    <div class="box-side__latch-top"></div>
    <div class="box-side__name">ROLO<br>FENU</div>
    <div class="box-side__jp">餃子専門店　新鮮手作り</div>
    <div class="box-side__tagline">INSPIRED BY JAPAN'S VIBRANT FOOD CULTURE</div>
  </section>
</body>
</html>
```